Coffee bag stamp design for new coffee brand

Stamp design that will be used like a label on a coffee package.
It must be a vector that can be produced as a stamp. Coffee bag is from brown craft paper. I upload image of this bag. Size of design is 80mm x 140mm.
I also uploaded two pictures for inspiration, but I will also appreciate new ideas.

Target Market(s)

Coffee lovers, who love to try new coffee. Also hipsters.

Colors

Designer to choose only greyscale colors for use in the design.

Requirements
Must have
• Some information about coffee must have:
Name: BRAZIL (the biggest font in that design)
Region: Santos
Altitude: 60 – 1200 m.n.m.
Variety: Arabica
Processing: unwashed

```html
<!DOCTYPE html>
<html lang="en">
<head>
<meta charset="utf-8">
<title>Brazil Santos – Coffee Bag Stamps</title>
<link rel="stylesheet" href="https://fonts.googleapis.com/css2?family=Josefin+Sans:wght@600;700&display=swap">
<style>
  :root {
    --kraft: #cfae8c;
    --kraft-shade: #c29f7c;
    --ink: #3a3331;
    --ink-soft: rgba(58, 51, 49, 0.14);
  }
  html, body {
    margin: 0;
    padding: 0;
    width: 1200px;
    height: 791px;
    overflow: hidden;
    background: var(--kraft);
    font-family: "Josefin Sans", sans-serif;
    color: var(--ink);
  }
  .canvas {
    position: relative;
    width: 1200px;
    height: 791px;
  }
  .stamp {
    position: absolute;
    box-sizing: border-box;
  }
  .stamp--framed {
    left: 205px; top: 330px; width: 202px; height: 362px;
    border: 2px solid var(--ink);
    padding: 4px;
  }
  .stamp--framed .inner-frame {
    width: 100%; height: 100%;
    border: 2px solid var(--ink);
    box-sizing: border-box;
    position: relative;
  }
  .stamp--open {
    left: 495px; top: 340px; width: 210px; height: 350px;
  }
  .stamp--dashed {
    left: 792px; top: 332px; width: 202px; height: 360px;
    border: 3px solid var(--ink);
  }
  .stamp--dashed .dash-frame {
    position: absolute; inset: 6px;
    border: 3px dashed var(--ink);
  }

  .brand {
    position: absolute;
    display: flex;
    flex-direction: column;
    align-items: center;
    gap: 2px;
  }
  .brand-dot {
    width: 16px; height: 16px;
    border: 1.5px solid var(--ink);
    border-radius: 50%;
    box-sizing: border-box;
  }
  .brand-name {
    font-weight: 700;
    font-size: 6px;
    letter-spacing: 0.5px;
    text-transform: uppercase;
    line-height: 1.1;
    text-align: center;
  }

  .coffee-facts {
    position: absolute;
    line-height: 1;
    text-transform: uppercase;
    font-weight: 700;
  }
  .coffee-facts p { margin: 0; display: flex; align-items: center; gap: 2px; }
  .origin-name { letter-spacing: 0.5px; }
  .facts-altitude { font-weight: 600; }
  .facts-process { font-weight: 600; letter-spacing: 0.6px; }
  .icon { fill: var(--ink); flex: none; }

  .coffee-facts--small { right: 14px; top: 14px; align-items: flex-start; }
  .coffee-facts--small .origin-name { font-size: 19px; }
  .coffee-facts--small .facts-region { font-size: 14px; }
  .coffee-facts--small .facts-altitude { font-size: 7px; margin: 1px 0; }
  .coffee-facts--small .facts-variety { font-size: 17px; }
  .coffee-facts--small .facts-process { font-size: 6.5px; margin-top: 2px; padding-left: 6px; }

  .coffee-facts--open { left: 16px; top: 222px; }
  .coffee-facts--open .origin-name { font-size: 18px; }
  .coffee-facts--open .facts-region { font-size: 13px; }
  .coffee-facts--open .facts-altitude { font-size: 7px; margin: 1px 0; }
  .coffee-facts--open .facts-variety { font-size: 16px; }
  .coffee-facts--open .facts-process { font-size: 6.5px; margin-top: 2px; }

  .coffee-facts--large { left: 0; right: 0; top: 92px; display: flex; flex-direction: column; align-items: center; }
  .coffee-facts--large .origin-name { font-size: 27px; }
  .coffee-facts--large .facts-region { font-size: 20px; }
  .coffee-facts--large .facts-altitude { font-size: 8.5px; margin: 2px 0; }
  .coffee-facts--large .facts-variety { font-size: 24px; }
  .coffee-facts--large .facts-process { font-size: 8px; margin-top: 2px; }

  .plant {
    position: absolute;
    background: var(--ink-soft);
    border-radius: 4px;
  }
  .stamp--framed .plant { left: 40px; top: 140px; width: 116px; height: 196px; }
  .stamp--open .plant { left: 30px; top: 0; width: 180px; height: 350px; }
  .stamp--dashed .plant { left: 68px; top: 220px; width: 66px; height: 120px; }
  .stamp--open .coffee-facts, .stamp--open .brand { z-index: 1; }
</style>
</head>
<body>
<main class="canvas">

  <!-- Variant one: double frame -->
  <section class="stamp stamp--framed">
    <div class="inner-frame">
      <div class="brand" style="left:12px; top:22px;">
        <span class="brand-dot"></span>
        <span class="brand-name">Lumen<br>Coffee</span>
      </div>
      <div class="coffee-facts coffee-facts--small">
        <p class="origin-name">Brazil</p>
        <p class="facts-region"><svg class="icon" width="8" height="11" viewBox="0 0 8 11"><path d="M4 0a4 4 0 0 0-4 4c0 3 4 7 4 7s4-4 4-7a4 4 0 0 0-4-4zm0 5.6a1.6 1.6 0 1 1 0-3.2 1.6 1.6 0 0 1 0 3.2z"/></svg>Santos</p>
        <p class="facts-altitude"><svg class="icon" width="9" height="6" viewBox="0 0 9 6"><path d="M0 6l3-5 2 3 1-1.5L9 6z"/></svg>60 – 1200 m.n.m.</p>
        <p class="facts-variety">Arabica</p>
        <p class="facts-process">Unwashed <svg class="icon" width="7" height="5" viewBox="0 0 7 5"><ellipse cx="3.5" cy="2.5" rx="3.5" ry="2.5"/></svg></p>
      </div>
      <div class="plant" role="img" aria-label="Line drawing of a coffee plant branch with leaves and cherries"></div>
    </div>
  </section>

  <!-- Variant two: open layout with large branch -->
  <section class="stamp stamp--open">
    <div class="plant" role="img" aria-label="Large line drawing of a coffee plant branch with leaves and cherries"></div>
    <div class="brand" style="left:52px; top:188px;">
      <span class="brand-dot"></span>
      <span class="brand-name">Lumen<br>Coffee</span>
    </div>
    <div class="coffee-facts coffee-facts--open">
      <p class="origin-name">Brazil</p>
      <p class="facts-region"><svg class="icon" width="8" height="11" viewBox="0 0 8 11"><path d="M4 0a4 4 0 0 0-4 4c0 3 4 7 4 7s4-4 4-7a4 4 0 0 0-4-4zm0 5.6a1.6 1.6 0 1 1 0-3.2 1.6 1.6 0 0 1 0 3.2z"/></svg>Santos</p>
      <p class="facts-altitude"><svg class="icon" width="9" height="6" viewBox="0 0 9 6"><path d="M0 6l3-5 2 3 1-1.5L9 6z"/></svg>60 – 1200 m.n.m.</p>
      <p class="facts-variety">Arabica</p>
      <p class="facts-process"><svg class="icon" width="7" height="5" viewBox="0 0 7 5"><ellipse cx="3.5" cy="2.5" rx="3.5" ry="2.5"/></svg> Unwashed <svg class="icon" width="7" height="5" viewBox="0 0 7 5"><ellipse cx="3.5" cy="2.5" rx="3.5" ry="2.5"/></svg></p>
    </div>
  </section>

  <!-- Variant three: dashed frame, centred -->
  <section class="stamp stamp--dashed">
    <div class="dash-frame"></div>
    <div class="brand" style="left:0; right:0; top:34px;">
      <span class="brand-dot" style="width:20px;height:20px;"></span>
      <span class="brand-name">Lumen Coffee</span>
    </div>
    <div class="coffee-facts coffee-facts--large">
      <p class="origin-name">Brazil</p>
      <p class="facts-region"><svg class="icon" width="10" height="14" viewBox="0 0 8 11"><path d="M4 0a4 4 0 0 0-4 4c0 3 4 7 4 7s4-4 4-7a4 4 0 0 0-4-4zm0 5.6a1.6 1.6 0 1 1 0-3.2 1.6 1.6 0 0 1 0 3.2z"/></svg>Santos</p>
      <p class="facts-altitude"><svg class="icon" width="10" height="7" viewBox="0 0 9 6"><path d="M0 6l3-5 2 3 1-1.5L9 6z"/></svg>60 – 1200 m.n.m.</p>
      <p class="facts-variety">Arabica</p>
      <p class="facts-process"><svg class="icon" width="8" height="6" viewBox="0 0 7 5"><ellipse cx="3.5" cy="2.5" rx="3.5" ry="2.5"/></svg> Unwashed <svg class="icon" width="8" height="6" viewBox="0 0 7 5"><ellipse cx="3.5" cy="2.5" rx="3.5" ry="2.5"/></svg></p>
    </div>
    <div class="plant" role="img" aria-label="Small line drawing of a coffee plant branch with leaves and cherries"></div>
  </section>

</main>
</body>
</html>
```